Ridgeway Coverage Partners
Business Card, Stationary, Folder jacket, Envelope
Project: Ridgeway Coverage Partners
Ridgeway Coverage Partners -
Creative Brief
Simple
Roy Fenwick
Insurance Professional
24517 Marrow Ave, Suite 400 Dunmere, UT 84921
SLC: 801-555-0143
Direct: 801-555-0178
Roy@RCPquarry.example
www.RCPquarry.example
Utah License No. 718260
We will need a space for a photo to be placed. Also, we will need the ability to customize the card for our different employees as needed. All personal info needs to be editable.
Open to ideas but we may want to have logos for the different insurance companies that we sell for. Examples: The Brellmont, Quorvia auto and home, Pennowick Insurance, Dralle, Tovrin, Ashbrook, TRVL, Wendiver, Pollick, Brisco, Fennimore Casualty, Vale Drivers...

```html
<!DOCTYPE html>
<html lang="en">
<head>
<meta charset="utf-8">
<title>Ridgeway Coverage Partners – Stationery Set</title>
<link href="https://fonts.googleapis.com/css2?family=Montserrat:wght@400;600;700&display=swap" rel="stylesheet">
<style>
  :root{
    --bg:#3b3b3d;
    --bg-deep:#2a2a2c;
    --red:#a3162b;
    --red-dark:#6e0c1a;
    --ink:#2c2c2c;
    --grey:#8a8a8a;
    --paper:#ffffff;
    --faint:#ececec;
    --slate:#4b5564;
  }
  *{box-sizing:border-box;margin:0;padding:0}
  html,body{width:1200px;height:310px;overflow:hidden}
  body{background:radial-gradient(ellipse at 50% 40%,var(--bg),var(--bg-deep));font-family:"Montserrat",sans-serif;position:relative;color:var(--ink)}
  .piece{position:absolute;background:var(--paper);box-shadow:0 2px 5px rgba(0,0,0,.45);overflow:hidden}
  .brand{display:flex;align-items:center;gap:4px;font-weight:700;text-transform:uppercase;line-height:1.05}
  .brand .mark{width:10px;height:10px;background:var(--red);flex:none}
  .brand .name{color:var(--red);font-size:6px;letter-spacing:.3px}
  .brand.light .name{color:#fff}
  .tiny{font-size:3.2px;line-height:1.5;color:var(--grey)}
  .watermark{position:absolute;border-radius:50%;background:var(--faint)}
  /* cards */
  .card{width:101px;height:42px}
  .card--front-dark{left:12px;top:7px;width:209px;height:89px;background:linear-gradient(135deg,#3a3a3d,#1f1f21)}
  .card--front-dark .brand{position:absolute;left:14px;top:10px}
  .card--front-dark .brand .mark{width:16px;height:16px}
  .card--front-dark .brand .name{font-size:9px}
  .card--front-dark .tagline{position:absolute;left:34px;top:34px;font-size:4px;color:#bbb}
  .card--front-dark .carriers{position:absolute;left:14px;top:50px;font-size:4px;color:#fff;background:var(--red);padding:2px 5px}
  .card--split{top:102px}
  .card--split .band{position:absolute;left:0;top:0;width:52px;height:100%;background:linear-gradient(135deg,var(--red),var(--red-dark))}
  .card--split .photo{position:absolute;left:12px;top:8px;width:26px;height:26px;background:linear-gradient(#c44a5a,#8a1626)}
  .card--split .info{position:absolute;left:56px;top:6px}
  .card--split .info b{display:block;font-size:4px;color:var(--ink)}
  .card--white{top:192px}
  .card--white .brand{position:absolute;left:8px;top:12px}
  .card--white .info{position:absolute;left:8px;top:6px}
  .card--white .info b{display:block;font-size:4px;color:var(--red)}
  /* letterheads */
  .letter{top:7px;width:240px;height:292px}
  .letter--edge{left:235px;border-left:4px solid var(--red)}
  .letter--edge .brand{position:absolute;left:16px;top:12px}
  .letter--edge .contact{position:absolute;right:14px;top:14px;text-align:right}
  .letter--band{left:490px;width:236px}
  .letter--band .brand{position:absolute;left:50px;top:14px}
  .letter--band .contact{position:absolute;right:14px;top:16px;text-align:right}
  .letter--band .foot{position:absolute;left:0;bottom:0;width:100%;height:8px;background:linear-gradient(90deg,var(--red-dark),var(--red))}
  .letter .web{position:absolute;bottom:12px;width:100%;text-align:center}
  /* envelopes */
  .envelope{left:747px;top:103px;width:200px;height:112px}
  .envelope .brand{position:absolute;left:8px;top:8px}
  .envelope .contact{position:absolute;left:22px;top:22px}
  .envelope .foot{position:absolute;left:0;bottom:0;width:100%;height:10px;background:linear-gradient(90deg,var(--red-dark),var(--red))}
  .envelope-stack{position:absolute;left:958px;top:22px;width:236px;height:258px}
</style>
</head>
<body>

  <!-- business cards -->
  <section class="piece card--front-dark" aria-label="Business card front">
    <div class="brand light"><span class="mark"></span><span class="name">Ridgeway<br>Coverage Partners</span></div>
    <p class="tagline">Protecting what matters most</p>
    <p class="carriers">Carriers we represent</p>
  </section>

  <section class="piece card card--split" style="left:12px" aria-label="Business card back">
    <div class="band"></div>
    <div class="photo" role="img" aria-label="Space for employee photo"></div>
    <div class="info tiny"><b>Roy Fenwick</b>Insurance Professional<br>SLC: 801-555-0143<br>Direct: 801-555-0178<br>Roy@RCPquarry.example</div>
  </section>

  <section class="piece card card--split" style="left:120px" aria-label="Business card back variant">
    <div class="band"></div>
    <div class="photo" role="img" aria-label="Space for employee photo"></div>
    <div class="info tiny"><b>Roy Fenwick</b>Insurance Professional<br>www.RCPquarry.example<br>Utah License No. 718260</div>
  </section>

  <section class="piece card card--white" style="left:12px" aria-label="Business card front light">
    <div class="brand"><span class="mark"></span><span class="name">Ridgeway<br>Coverage Partners</span></div>
  </section>

  <section class="piece card card--white" style="left:120px" aria-label="Business card contact side">
    <div class="info tiny"><b>Roy Fenwick</b>Insurance Professional<br>24517 Marrow Ave, Suite 400<br>Dunmere, UT 84921<br>SLC: 801-555-0143 · Direct: 801-555-0178<br>Roy@RCPquarry.example</div>
  </section>

  <!-- letterheads -->
  <section class="piece letter letter--edge" aria-label="Letterhead">
    <div class="brand"><span class="mark"></span><span class="name">Ridgeway<br>Coverage Partners</span></div>
    <p class="contact tiny">24517 Marrow Ave, Suite 400<br>Dunmere, UT 84921<br>801-555-0143</p>
    <div class="watermark" style="left:70px;top:100px;width:96px;height:96px"></div>
    <p class="web tiny">www.RCPquarry.example</p>
  </section>

  <section class="piece letter letter--band" aria-label="Letterhead alternate">
    <div class="brand"><span class="mark"></span><span class="name">Ridgeway<br>Coverage Partners</span></div>
    <p class="contact tiny">24517 Marrow Ave, Suite 400<br>Dunmere, UT 84921<br>801-555-0143</p>
    <div class="watermark" style="left:70px;top:100px;width:96px;height:96px"></div>
    <p class="web tiny" style="bottom:14px">www.RCPquarry.example</p>
    <div class="foot"></div>
  </section>

  <!-- envelope front -->
  <section class="piece envelope" aria-label="Envelope front">
    <div class="brand"><span class="mark"></span><span class="name">Ridgeway<br>Coverage Partners</span></div>
    <p class="contact tiny">24517 Marrow Ave, Suite 400<br>Dunmere, UT 84921</p>
    <div class="foot"></div>
  </section>

  <!-- envelope backs -->
  <svg class="envelope-stack" viewBox="0 0 236 258" aria-label="Envelope backs">
    <g>
      <rect x="2" y="2" width="232" height="86" fill="#e9e9ec"/>
      <polygon points="2,2 234,2 118,40" fill="var(--slate)"/>
    </g>
    <g>
      <rect x="2" y="70" width="232" height="86" fill="#f1f1f1"/>
      <polygon points="2,70 234,70 118,112" fill="var(--red)"/>
    </g>
    <g>
      <rect x="2" y="150" width="232" height="100" fill="#fafafa" stroke="#ddd" stroke-width=".5"/>
      <polygon points="2,150 234,150 118,196" fill="#f0f0f0" stroke="#d6d6d6" stroke-width=".6"/>
      <rect x="109" y="183" width="18" height="18" fill="var(--red)"/>
    </g>
  </svg>

</body>
</html>
```